International Manufacturing Business Needs A Heavy Hitting Wordpress Design!

We need wordpress template designs for a new website for our UK based International company Tolvane Engineering Ltd. We manufacture and supply steel security doors and window units. We would like designs that feature the black and yellow industrial "stripes" that can be seen at our current site www.tolvadoors.com. The final design should communicate strength, power and weight to represent the quality of the products and the security that they provide.

It feels like we need 3 different types of page to be able to be created as per the current website at www.tolvasecuredoors.com.

Homepage
Products/Accessories
Leadtimes/Downloads/Contact

It may be that 3 different page types can be created with one template. I'm totally open to this.

I don't like the way that the site currently handles product images, nobody wants to click on even thumbnail to see the product. http://tolvasecuredoors.com/products/personnel-doors/

Totally open to suggestions on layout to enable the feeling outlined in the brief above.

Please ask if anything is not clear or you need answers to drill down on specifics.

Sick

Target Market(s)

Businesses that buy steel doors

Font styles to use
Sans Serif
Other font styles liked:
• Copperplate Gothic Bold - For Company Name but we are open to suggestions

Colors

Designer to choose colors to be used in the design.

Requirements
Must have
• Professional looking, clean design
• Conveys strength, power and weight to represent the quality of the products, the characteristics of steel and the security that they provide.
• Incorporates black and yellow stripes of our branding
• Ability to create pages with content as seen at www.tolvasecuredoors.com
• A better way of showing the product images
Nice to have
• If possible. a design that gives off the feeling that not only do we supply the products we also make them in house too. I don't know what this looks like but a way of differentiating between a supply only business and one that manufacturers the product too.
Should not have
• We don't like the current thumbnail method of showing the product images

```html
<!DOCTYPE html>
<html lang="en">
<head>
<meta charset="utf-8">
<title>Tolvane Engineering Ltd</title>
<link href="https://fonts.googleapis.com/css2?family=Questrial&family=Arimo:wght@400;700&display=swap" rel="stylesheet">
<style>
:root{
  --navy:#17222f;
  --navy-deep:#0f1720;
  --footer:#1a2533;
  --footer-bar:#0c1219;
  --yellow:#f5e20c;
  --teal:#3f8b93;
  --teal-btn:#5b9a98;
  --ink:#222;
  --white:#fff;
  --grey-tile:#d3d3d3;
}
*{margin:0;padding:0;box-sizing:border-box}
html,body{width:1200px;height:3681px;overflow:hidden}
body{position:relative;background:var(--white);font-family:"Arimo",Arial,sans-serif;color:var(--ink)}
.abs{position:absolute}
.photo{position:absolute}

/* header */
.hero{position:absolute;left:0;top:0;width:1200px;height:610px;
  background:linear-gradient(180deg,#2c3550 0%,#6a5a78 18%,#3a3f4c 40%,#2a2d31 70%,#16181b 100%)}
.topbar{position:absolute;left:0;top:0;width:1200px;height:70px;background:rgba(15,23,32,.55)}
.brand{position:absolute;left:88px;top:17px;display:flex;align-items:center;gap:10px;color:var(--white);
  font-family:"Questrial",sans-serif;font-size:17px;letter-spacing:1px;line-height:1.05}
.brand-mark{width:20px;height:34px;background:var(--teal)}
.brand small{display:block;font-size:10px;letter-spacing:1.5px}
.nav a{position:absolute;top:28px;color:var(--white);font-size:12px;text-decoration:none;letter-spacing:.5px}
.nav-products{position:absolute;left:600px;top:0;width:112px;height:124px;background:var(--yellow)}
.nav-products span{position:absolute;left:0;width:112px;top:28px;text-align:center;font-size:12px;color:#333}
.dropdown{position:absolute;left:600px;top:70px;width:112px;font-size:10.5px;color:#333;padding:14px 0 0 20px;line-height:26px}
.submenu{position:absolute;left:712px;top:70px;width:135px;height:156px;background:var(--yellow);
  font-size:10px;color:#333;padding:8px 0 0 12px;line-height:17px}
.download{position:absolute;left:842px;top:24px;width:128px;height:24px;background:var(--teal-btn);
  color:var(--white);font-size:10px;letter-spacing:1px;text-align:center;line-height:24px}
.social{position:absolute;left:1004px;top:25px;display:flex;gap:6px}
.social i{display:block;width:20px;height:20px;background:#4a6fa8;border-radius:3px}
.social i:nth-child(2){background:#38a1d8}
.social i:nth-child(3){background:#c8234a}
.social i:nth-child(4){background:#b23d8c}
.hero-tag{position:absolute;left:650px;top:440px;width:550px;height:112px;background:rgba(0,0,0,.55)}
.hero-kicker{position:absolute;right:66px;top:456px;color:var(--white);font-family:"Questrial",sans-serif;font-size:22px;letter-spacing:1px}
.hero-title{position:absolute;right:66px;top:486px;color:var(--white);font-family:"Questrial",sans-serif;font-size:40px}
.stripes{position:absolute;left:0;top:590px}

/* what we do */
h2.section-title{position:absolute;left:417px;top:706px;font-family:"Questrial",sans-serif;font-weight:400;
  font-size:30px;color:var(--teal);letter-spacing:1px}
ul.points{position:absolute;font-size:16.5px;line-height:24px;padding-left:20px}
ul.points li{margin-bottom:2px}
.intro-points{left:418px;top:788px;width:620px;color:#333}

.features{position:absolute;left:0;top:1043px;width:1200px;height:552px;background:var(--navy)}
.feature-points{left:160px;top:1157px;width:400px;color:var(--white)}
.btn-outline{position:absolute;height:32px;font-size:11px;letter-spacing:.5px;text-align:center;line-height:30px}
.more{left:191px;top:1443px;width:256px;background:var(--white);color:#333;border:1px solid #bbb}

.slider{position:absolute;left:0;top:1595px;width:1200px;height:520px;
  background:linear-gradient(90deg,#2a3036 0%,#1c2025 35%,#0f1216 70%,#0a0c0f 100%)}
.slide-title{position:absolute;left:584px;top:1765px;font-family:"Questrial",sans-serif;font-size:56px;color:var(--yellow)}
.slide-text{position:absolute;left:584px;top:1834px;width:530px;font-size:14px;line-height:20px;color:#e6e6e6}
.interested{left:584px;top:1907px;width:164px;height:29px;line-height:27px;border:1px solid #8b7f1a;color:#eee;font-size:11px}
.dots{position:absolute;left:563px;top:2072px;display:flex;gap:18px}
.dots i{display:block;width:13px;height:13px;border-radius:50%;background:#bbb}

.category-title{position:absolute;width:405px;text-align:center;font-family:"Questrial",sans-serif;font-size:33px;color:var(--teal);top:2565px}
.category-text{position:absolute;width:405px;text-align:center;font-size:15.5px;line-height:24px;color:#333;top:2620px}

.products-title{position:absolute;left:0;width:1200px;top:2758px;text-align:center;font-family:"Questrial",sans-serif;font-size:58px;color:var(--ink)}
.tile{position:absolute;width:261px;height:258px;background:var(--grey-tile);border:1px solid #c3c3c3;
  display:flex;align-items:center;justify-content:center;font-size:21px;color:#222}
.tile-label{color:var(--white);font-weight:700;text-align:center;line-height:30px}

.footer{position:absolute;left:0;top:3504px;width:1200px;height:123px;background:var(--footer)}
.footer-brand{left:160px;top:3542px}
.address{position:absolute;left:415px;top:3538px;width:200px;text-align:center;color:var(--white);font-size:17px;line-height:25px}
.badge{position:absolute;top:3538px;height:55px}
.footer-bar{position:absolute;left:0;top:3627px;width:1200px;height:54px;background:var(--footer-bar)}
.copyright{position:absolute;left:165px;top:3648px;color:#ccc;font-size:10px;letter-spacing:.3px}
.footer-social{left:1004px;top:3644px}
</style>
</head>
<body>

<!-- header / hero -->
<div class="hero photo" role="img" aria-label="Modern two-storey house with large glass windows at dusk"></div>
<div class="topbar"></div>
<div class="brand"><div class="brand-mark"></div><div>TOLVANE<small>ENGINEERING LTD.</small></div></div>
<nav class="nav">
  <a style="left:538px">HOME</a>
  <div class="nav-products"><span>PRODUCTS</span></div>
  <div class="dropdown"><div>Products &nbsp;&nbsp;&nbsp;&nbsp;»</div><div>Accessories &nbsp;»</div></div>
  <div class="submenu">
    <div>• Personnel Doors</div><div>• Fire Exit Doors</div><div>• Blank Doors</div><div>• Acoustic Doors</div>
    <div>• Anti-vandal shutters<br>&nbsp;&nbsp;and glazing unit</div><div>• Technical Videos</div>
  </div>
  <a style="left:731px">CONTACT</a>
</nav>
<div class="download">DOWNLOAD</div>
<div class="social"><i></i><i></i><i></i><i></i></div>
<div class="hero-tag"></div>
<div class="hero-kicker">TOLVANE ENGINEERING,</div>
<div class="hero-title">Design to Your Family!</div>
<svg class="stripes" width="1200" height="20" viewBox="0 0 1200 20">
  <polygon fill="#f5e20c" points="152,0 252,0 240,20 140,20"/>
  <polygon fill="#f5e20c" points="405,0 545,0 533,20 393,20"/>
  <polygon fill="#f5e20c" points="655,0 800,0 788,20 643,20"/>
  <polygon fill="#f5e20c" points="945,0 1085,0 1073,20 933,20"/>
</svg>

<!-- what we do -->
<div class="photo" style="left:110px;top:610px;width:246px;height:408px;background:linear-gradient(90deg,#f4f4f4 0%,#cfd3d8 40%,#8e959c 55%,#e9ecef 80%,#fff 100%)" role="img" aria-label="Steel door lock with chrome handle"></div>
<h2 class="section-title">WHAT WE DO</h2>
<ul class="points intro-points">
  <li>Tolvane security doors combine a high level of security with exceptional value.</li>
  <li>Our superior quality and proven reliability has made us the first choice for a wide range of companies no matter what their requirement or application.</li>
  <li>All of our products are designed and manufactured to the highest specification, combine this with a rigorous quality control system and an extensive after-sales service and it is easy to see why we are seen as industry leaders.</li>
</ul>

<!-- features -->
<section class="features"></section>
<ul class="points feature-points">
  <li>We place particular emphasis on continuous development and twelve years experience ensures that we are always ahead of the competition and that we can react quickly to customer's requirements.</li>
  <li>Each and every Tolvane product is subject to our fifty point quality control process before it is dispatched.</li>
  <li>Tolvane have forged a reputation for affordable, high quality steel doors.</li>
</ul>
<div class="btn-outline more">MORE DETAILS</div>
<div class="photo" style="left:658px;top:1117px;width:348px;height:478px;background:linear-gradient(180deg,#2c4f8a 0%,#24467e 60%,#1d3a68 100%)" role="img" aria-label="Blue steel personnel door with vision panel"></div>

<!-- slider -->
<section class="slider" role="img" aria-label="Close-up of anti-vandal shroud fitted on a dark steel door"></section>
<div class="slide-title">Anti-Vandal Shroud</div>
<p class="slide-text">Tolvane Engineering's anti-vandal shroud has been designed to offer increased security protection for the standard 10-point locking personnel door.</p>
<div class="btn-outline interested">I'M INTERESTED!</div>
<div class="dots"><i></i><i></i><i></i></div>

<!-- categories -->
<div class="photo" style="left:184px;top:2204px;width:405px;height:331px;background:linear-gradient(90deg,#b3161c 0%,#d42a2a 50%,#7a0e10 80%,#111 100%)" role="img" aria-label="Red security door with lock and keys"></div>
<div class="photo" style="left:611px;top:2204px;width:405px;height:331px;background:linear-gradient(90deg,#0c0c0c 0%,#1a1a1a 55%,#d8c400 75%,#0a0a0a 100%)" role="img" aria-label="Fire exit push bar on yellow door frame"></div>
<h3 class="category-title" style="left:184px">Security Doors</h3>
<h3 class="category-title" style="left:611px">Fire Exit Doors</h3>
<p class="category-text" style="left:184px">Affordable steel personnel doors that do not<br>compromise on quality or security.</p>
<p class="category-text" style="left:611px">The same high quality Tolvane door available<br>with a range of fire exit hardware.</p>

<!-- products grid -->
<h2 class="products-title">Our Products</h2>
<div class="tile" style="left:184px;top:2871px;background:linear-gradient(90deg,#8e1a1a,#a82222 60%,#7a1414)" role="img" aria-label="Red louvred personnel door"><span class="tile-label">Personnel<br>Doors</span></div>
<div class="tile" style="left:471px;top:2871px;background:linear-gradient(90deg,#f2f2f2,#dedede 60%,#bfbfbf)" role="img" aria-label="White fire exit door with push bar"></div>
<div class="tile" style="left:756px;top:2871px">Photo</div>
<div class="tile" style="left:184px;top:3158px">Photo</div>
<div class="tile" style="left:471px;top:3158px;background:linear-gradient(180deg,#b9bcbe,#9fa3a6)" role="img" aria-label="Grey steel double access doors"></div>
<div class="tile" style="left:756px;top:3158px">Photo</div>

<!-- footer -->
<footer class="footer"></footer>
<div class="brand footer-brand"><div class="brand-mark"></div><div>TOLVANE<small>ENGINEERING LTD.</small></div></div>
<div class="address">Harrowby Lane, Elstead,<br>Hull, HU14 3QD</div>
<div class="badge" style="left:731px;width:80px;background:#f2f2f2"></div>
<div class="badge" style="left:816px;width:80px;background:#e4e4e4"></div>
<div class="badge" style="left:901px;width:117px;background:#8a5a3c"></div>
<div class="footer-bar"></div>
<div class="copyright">© Copyright 2018 &nbsp;|&nbsp; TOLVANE ENGINEERING</div>
<div class="social footer-social"><i></i><i></i><i></i><i></i></div>

</body>
</html>
```